Film and TV production company

I have the logo already designed by mark quarry. I just need the text and the logo attached to the business card. Maybe a small design on the back of the card or text.

Industry/Entity Type

film tv arts

Contact Information for Business Card

Dale Morrow Cinematographer-Director

Colors
F0912C
F2A743
F7CA91
FBE8D2
FDF5EE
EE7325
F08F49
F5BC92
FAE3D3
FDF4ED

Requirements
Must have
• www.copperlanepix.com.au my email address mail@copperlanepix.com.au my mobile number 0491570158
Nice to have
• Some kind of small art work on the back that ties in with the logo design attached
Should not have
• Must clean and simple

```html
<!DOCTYPE html>
<html lang="en">
<head>
<meta charset="utf-8">
<title>Copper Lane Pix – Business Card</title>
<link href="https://fonts.googleapis.com/css2?family=Barlow:wght@400;500&display=swap" rel="stylesheet">
<style>
  :root {
    --orange: #EE7325;
    --cream: #FDF5EE;
    --ink: #1E1E1E;
    --white: #FFFFFF;
  }
  html, body {
    margin: 0;
    padding: 0;
    overflow: hidden;
  }
  body {
    width: 1050px;
    height: 1200px;
    font-family: "Barlow", sans-serif;
  }
  .card {
    position: relative;
    width: 1050px;
    height: 1200px;
    background: var(--cream);
    overflow: hidden;
  }
  .card-back {
    position: absolute;
    left: 0; top: 0;
    width: 1050px;
    height: 598px;
    background: var(--orange);
  }
  .brand-mark {
    position: absolute;
    border-radius: 50%;
  }
  .brand-mark--large {
    left: 437px; top: 176px;
    width: 176px; height: 176px;
    background: var(--cream);
  }
  .brand-name {
    position: absolute;
    margin: 0;
    font-weight: 500;
    white-space: nowrap;
    text-transform: uppercase;
  }
  .brand-name--large {
    left: 0; width: 1050px;
    top: 356px;
    text-align: center;
    font-size: 44px;
    letter-spacing: 7px;
    color: var(--white);
  }
  .name-block {
    position: absolute;
    left: 0; top: 621px;
    width: 562px; height: 138px;
    background: var(--orange);
    color: var(--white);
  }
  .person-name {
    position: absolute;
    left: 36px; top: 4px;
    margin: 0;
    font-size: 78px;
    font-weight: 500;
    letter-spacing: 1px;
    line-height: 1.2;
  }
  .person-role {
    position: absolute;
    left: 99px; top: 86px;
    margin: 0;
    font-size: 29px;
    font-weight: 400;
    letter-spacing: 1px;
  }
  .brand-mark--small {
    left: 854px; top: 621px;
    width: 96px; height: 96px;
    background: var(--orange);
  }
  .brand-name--small {
    left: 760px; width: 284px;
    top: 720px;
    text-align: center;
    font-size: 26px;
    letter-spacing: 3px;
    color: var(--ink);
  }
  .contact-list {
    position: absolute;
    left: 39px; top: 783px;
    margin: 0; padding: 0;
    list-style: none;
  }
  .contact-item {
    display: flex;
    align-items: center;
    height: 60px;
    margin-bottom: 27px;
    color: var(--orange);
    font-size: 42px;
    font-weight: 500;
    letter-spacing: 1px;
  }
  .contact-icon {
    width: 60px; height: 60px;
    margin-right: 25px;
    flex: none;
  }
  .web-block {
    position: absolute;
    left: 488px; top: 1111px;
    width: 562px; height: 87px;
    background: var(--orange);
    color: var(--white);
    font-size: 42px;
    font-weight: 500;
    letter-spacing: 1px;
    line-height: 87px;
    text-align: right;
    padding-right: 36px;
    box-sizing: border-box;
  }
</style>
</head>
<body>
  <div class="card">
    <section class="card-back">
      <div class="brand-mark brand-mark--large"></div>
      <p class="brand-name brand-name--large">Copper Lane Pix</p>
    </section>

    <div class="name-block">
      <h1 class="person-name">Dale Morrow</h1>
      <p class="person-role">Cinematographer-Director</p>
    </div>

    <div class="brand-mark brand-mark--small"></div>
    <p class="brand-name brand-name--small">Copper Lane Pix</p>

    <ul class="contact-list">
      <li class="contact-item">
        <svg class="contact-icon" viewBox="0 0 60 60" aria-hidden="true">
          <circle cx="30" cy="30" r="30" fill="var(--orange)"/>
          <rect x="16" y="20" width="28" height="20" fill="none" stroke="#fff" stroke-width="2.5"/>
          <polyline points="16,20 30,31 44,20" fill="none" stroke="#fff" stroke-width="2.5"/>
          <polyline points="16,40 26,29 M34,29 44,40" fill="none" stroke="#fff" stroke-width="2.5"/>
          <line x1="34" y1="29" x2="44" y2="40" stroke="#fff" stroke-width="2.5"/>
        </svg>
        mail@copperlanepix.com.au
      </li>
      <li class="contact-item">
        <svg class="contact-icon" viewBox="0 0 60 60" aria-hidden="true">
          <circle cx="30" cy="30" r="30" fill="var(--orange)"/>
          <path d="M21 16 l6 0 l3 8 l-4 3 q3 7 10 10 l3 -4 l8 3 l0 6 q-2 3 -6 3 q-14 -2 -22 -20 q-1 -6 2 -9z" fill="#fff"/>
        </svg>
        0491570158
      </li>
      <li class="contact-item">
        <svg class="contact-icon" viewBox="0 0 60 60" aria-hidden="true">
          <circle cx="30" cy="30" r="30" fill="var(--orange)"/>
          <path d="M30 47 q-12 -14 -12 -22 a12 12 0 0 1 24 0 q0 8 -12 22z" fill="#fff"/>
          <circle cx="30" cy="25" r="5" fill="var(--orange)"/>
        </svg>
        Your address Here
      </li>
    </ul>

    <div class="web-block">www.copperlanepix.com.au</div>
  </div>
</body>
</html>
```